Packaging design for a low carb bar

I am producing a low carb / high fat bar, therefore I would like to have a light weighted modern design. The background color pastel light or something like that. The package should be focused on fitness-active individuals who are looking for healthy low carb snacks. Preliminary packaging size, logo, and more details on what should be attached to the packaging are attached. Thank you!

```html
<!DOCTYPE html>
<html lang="en">
<head>
<meta charset="utf-8">
<title>Nutrava Keto Bar Label</title>
<link rel="stylesheet" href="https://fonts.googleapis.com/css2?family=Amatic+SC:wght@700&family=Montserrat:wght@800&family=Mulish:wght@300;600;800&display=swap">
<style>
  :root {
    --page: #e9eaeb;
    --white: #ffffff;
    --sky: #d8eef4;
    --blue: #1c8fc4;
    --blue-deep: #1277a8;
    --teal: #4f9fb0;
    --teal-light: #8cc7d3;
    --heart: #5d9fb1;
    --heart-ring: #a9d3dc;
    --olive: #c9b51e;
    --olive-ring: #e3d54c;
    --green: #4fb52b;
    --green-ring: #8ad55b;
    --food: #9b6a3e;
  }
  html, body {
    margin: 0;
    width: 1200px;
    height: 960px;
    overflow: hidden;
    background: var(--page);
  }
  .canvas {
    position: relative;
    width: 1200px;
    height: 960px;
  }
  .label {
    position: absolute;
    left: 465px;
    top: 30px;
    width: 270px;
    height: 900px;
    overflow: hidden;
    box-shadow: 0 6px 22px rgba(0,0,0,.18);
  }
  .label-art {
    position: absolute;
    inset: 0;
  }
  .brand {
    position: absolute;
    left: 0; right: 0;
    top: 106px;
    text-align: center;
    font-family: "Mulish", sans-serif;
    font-weight: 300;
    font-size: 26px;
    letter-spacing: 3px;
    color: var(--white);
  }
  .product-name {
    position: absolute;
    left: 0; right: 0;
    top: 232px;
    margin: 0;
    text-align: center;
    font-family: "Amatic SC", sans-serif;
    font-weight: 700;
    font-size: 112px;
    line-height: 92px;
    color: var(--white);
    letter-spacing: 2px;
  }
  .made-with {
    position: absolute;
    left: 14px;
    top: 462px;
    font-family: "Mulish", sans-serif;
    font-weight: 600;
    font-size: 12px;
    line-height: 13px;
    color: var(--white);
    text-align: center;
    transform: rotate(-18deg);
  }
  .flavours {
    position: absolute;
    left: 68px;
    top: 446px;
    font-family: "Montserrat", sans-serif;
    font-weight: 800;
    font-size: 21px;
    line-height: 32px;
    color: var(--white);
    letter-spacing: .5px;
  }
  .badge-text {
    position: absolute;
    font-family: "Mulish", sans-serif;
    font-weight: 800;
    color: var(--white);
  }
  .badge-keto {
    left: 48px; top: 660px;
    font-size: 10.5px; line-height: 13px;
  }
  .badge-carbs {
    left: 186px; top: 686px;
    width: 40px; text-align: center;
    font-size: 7px; line-height: 9px;
  }
  .badge-vegan {
    left: 105px; top: 790px;
    width: 80px; text-align: center;
    font-size: 15px;
  }
  .net-weight {
    position: absolute;
    left: 0; right: 0;
    top: 848px;
    text-align: center;
    font-family: "Mulish", sans-serif;
    font-weight: 800;
    font-size: 13.5px;
    color: var(--white);
  }
</style>
</head>
<body>
<div class="canvas">
  <div class="label">
    <svg class="label-art" width="270" height="900" viewBox="0 0 270 900" aria-hidden="true">
      <!-- top white panel -->
      <rect width="270" height="900" fill="var(--white)"/>
      <circle cx="135" cy="70" r="150" fill="var(--sky)" opacity=".35"/>
      <!-- upper blue band -->
      <path d="M0 222 Q12 214 24 222 T48 222 T72 222 T96 222 T120 222 T144 222 T168 222 T192 222 T216 222 T240 222 T264 222 L270 220 L270 628 Q258 636 246 628 T222 628 T198 628 T174 628 T150 628 T126 628 T102 628 T78 628 T54 628 T30 628 T6 628 L0 630 Z" fill="var(--blue)"/>
      <!-- lower blue band -->
      <path d="M0 800 Q12 792 24 800 T48 800 T72 800 T96 800 T120 800 T144 800 T168 800 T192 800 T216 800 T240 800 T264 800 L270 798 L270 900 L0 900 Z" fill="var(--blue-deep)"/>
      <!-- brand circle -->
      <circle cx="135" cy="120" r="72" fill="var(--teal-light)"/>
      <circle cx="135" cy="120" r="62" fill="var(--teal)"/>
      <!-- ingredients photo area -->
      <rect x="28" y="538" width="222" height="92" rx="30" fill="var(--food)" role="img" aria-label="Photo of halved coconut, almonds and peanuts"/>
      <!-- keto diet badge -->
      <circle cx="64" cy="668" r="64" fill="var(--heart-ring)" opacity=".8"/>
      <circle cx="70" cy="668" r="54" fill="var(--heart)"/>
      <path d="M2 652 H28 L34 640 L40 664 L46 630 L52 652 H60" fill="none" stroke="var(--white)" stroke-width="1.5"/>
      <path d="M74 648 C64 638 56 648 66 658 L74 666 L82 658 C92 648 84 638 74 648 Z" fill="none" stroke="var(--white)" stroke-width="1.5"/>
      <!-- net carbs badge -->
      <circle cx="205" cy="677" r="42" fill="var(--olive-ring)"/>
      <circle cx="205" cy="677" r="35" fill="var(--olive)"/>
      <g fill="none" stroke="var(--white)" stroke-width="1.6">
        <path d="M205 652 V680"/>
        <ellipse cx="199" cy="660" rx="4" ry="6"/>
        <ellipse cx="211" cy="660" rx="4" ry="6"/>
        <ellipse cx="199" cy="671" rx="4" ry="6"/>
        <ellipse cx="211" cy="671" rx="4" ry="6"/>
      </g>
      <!-- vegan badge -->
      <circle cx="145" cy="774" r="66" fill="var(--green-ring)"/>
      <circle cx="145" cy="774" r="55" fill="var(--green)"/>
      <path d="M133 784 C133 766 148 758 160 758 C160 774 150 784 133 784 Z" fill="var(--white)"/>
      <path d="M133 784 C140 776 148 770 156 764" stroke="var(--green)" stroke-width="1.5" fill="none"/>
    </svg>

    <div class="brand">NUTRAVA</div>
    <h1 class="product-name">KETO<br>BAR</h1>
    <div class="made-with">Made<br>With</div>
    <div class="flavours">ALMOND,<br>COCONUT<br>&amp; CHIA</div>
    <div class="badge-text badge-keto">Suitable<br>for a Keto /<br>LCHF Diet</div>
    <div class="badge-text badge-carbs">3.5g Net<br>Carbs</div>
    <div class="badge-text badge-vegan">Vegan</div>
    <div class="net-weight">Net Wt 1.7oz(49g)</div>
  </div>
</div>
</body>
</html>
```